FOLDER

I need a fine folder that will contain other items like brochures, flyers etc. This folder will be used to reach potential customers. The project will also include letter head
Updates

Please provide the following:
1. While we have the small envelop also include a big envelop that will contain the folder.
2. Please design a letterhead
3. Include in the design:
- Company name: Tarvo Cleaning & Facility Services Nigeria Limited.
- Our Logo. I have attached it.
- Moto: Setting new cleaning standards...
- Website: www.tarvo-cleaning.com.ng
- E-mail: nigeria@tarvo-cleaning.com
- Tel: 08127365904, 07069318472
Please give the size / dimensions of your designs (width and height).

Target Market(s)

households, offices etc. The business is cleaning and facility services

Requirements
Must have
• Please provide the following:
3. Include in the design:

```html
<!DOCTYPE html>
<html lang="en">
<head>
<meta charset="utf-8">
<title>Tarvo Cleaning – Stationery</title>
<link rel="stylesheet" href="https://fonts.googleapis.com/css2?family=Lato:wght@400;700&display=swap">
<style>
  :root {
    --backdrop: #96a0a4;
    --paper: #ffffff;
    --brand-blue: #1b2fd2;
    --rule-blue: #6d7ad8;
    --ink: #2a2a2a;
    --label: #ffffff;
  }
  * { box-sizing: border-box; margin: 0; padding: 0; }
  html, body { width: 1200px; height: 900px; overflow: hidden; }
  body {
    position: relative;
    background: var(--backdrop);
    font-family: "Lato", sans-serif;
    color: var(--ink);
  }
  .size-label {
    position: absolute;
    color: var(--label);
    font-size: 20px;
    letter-spacing: 1.5px;
  }
  .size-label--letterhead { left: 425px; top: 64px; }
  .size-label--envelope { left: 172px; top: 250px; }

  .sheet { position: absolute; background: var(--paper); }

  .envelope { left: 170px; top: 300px; width: 765px; height: 540px; }
  .letterhead { left: 613px; top: 69px; width: 496px; height: 700px; }

  .brand {
    position: absolute;
    display: flex;
    align-items: center;
    gap: 6px;
    color: var(--brand-blue);
    font-weight: 700;
    font-size: 28px;
    line-height: 1;
  }
  .brand__dot { width: 14px; height: 14px; border-radius: 50%; background: var(--brand-blue); }
  .envelope .brand { left: 25px; top: 42px; }
  .letterhead .brand { left: 25px; top: 42px; }

  .envelope__sender { position: absolute; left: 25px; top: 97px; font-size: 7.5px; line-height: 10px; }
  .company-name { font-weight: 700; }

  .letterhead__contact {
    position: absolute;
    right: 24px;
    top: 47px;
    text-align: right;
    font-size: 7.5px;
    line-height: 10.5px;
  }

  .rule { position: absolute; height: 1px; background: var(--rule-blue); }
  .envelope .rule { left: 23px; right: 24px; top: 517px; }
  .letterhead .rule--top { left: 23px; right: 24px; top: 95px; }
  .letterhead .rule--bottom { left: 23px; right: 24px; top: 664px; }

  .motto {
    position: absolute;
    left: 23px; right: 24px;
    top: 670px;
    text-align: center;
    font-size: 7.5px;
  }
</style>
</head>
<body>
  <p class="size-label size-label--letterhead">letterhead A4</p>
  <p class="size-label size-label--envelope">envelope 229mm x 324mm</p>

  <section class="sheet envelope" aria-label="Envelope 229 × 324 mm">
    <div class="brand"><span>Tarvo</span><span class="brand__dot"></span></div>
    <div class="envelope__sender">
      <p class="company-name">Tarvo Cleaning &amp; Facility Services Nigeria Limited</p>
      <p>www.tarvo-cleaning.com.ng</p>
    </div>
    <div class="rule"></div>
  </section>

  <section class="sheet letterhead" aria-label="Letterhead A4">
    <div class="brand"><span>Tarvo</span><span class="brand__dot"></span></div>
    <address class="letterhead__contact" style="font-style:normal">
      <p class="company-name">Tarvo Cleaning &amp; Facility Services Nigeria Limited</p>
      <p>tel: 08127365904, 07069318472</p>
      <p>nigeria@tarvo-cleaning.com</p>
      <p>www.tarvo-cleaning.com.ng</p>
    </address>
    <div class="rule rule--top"></div>
    <div class="rule rule--bottom"></div>
    <p class="motto">Setting new cleaning standards...</p>
  </section>
</body>
</html>
```